Looking for a creative label design for our retail coffee bags

We are a coffee manufacturer (coffee roaster) looking to re-brand our retail label for our coffee bags. Our main coffee blend that we sell is our Harborline Velvet Blend. You can use this name when creating the label. We are going for a look that represents our company as a coffee roaster. Please reference our website (www.brindlemugworks.com) and our Facebook page to learn more about our company and to give you more inspiration on creating this design.

Target Market(s)

Retail customers/grocery stores

Industry/Entity Type

Manufacturer

Requirements
Must have
• The size of the label has to be 3" width x 4" height

Logo must be Black
Nice to have
• We currently incorporate a color on our labels for each blend. For example, Harborline Velvet Blend (royal blue), Decaffeinated Blend (red), Breakfast Blend (green), Flavored coffees (gold).

Rustic/vintage style

```html
<!DOCTYPE html>
<html lang="en">
<head>
<meta charset="utf-8">
<title>Brindle Mugworks – Retail Coffee Labels</title>
<link rel="stylesheet" href="https://fonts.googleapis.com/css2?family=Roboto:wght@400;500;700&family=Dancing+Script:wght@500&display=swap">
<style>
  :root {
    --backdrop: #ebebeb;
    --label-green: #c4d57b;
    --breakfast: #4f5b33;
    --breakfast-text: #5a6339;
    --flavored: #2b2b2b;
    --decaf: #c0161d;
    --harborline: #0d57a6;
    --white: #ffffff;
  }
  * { box-sizing: border-box; margin: 0; padding: 0; }
  html, body { width: 1200px; height: 1200px; overflow: hidden; }
  body {
    background: var(--backdrop);
    position: relative;
    font-family: "Roboto", Arial, sans-serif;
  }

  .label {
    position: absolute;
    width: 40.6em;
    height: 54.4em;
    background: var(--label-green);
    overflow: hidden;
  }
  .label--large { font-size: 10px; left: 181px; top: 460px; }
  .label--small { font-size: 6.28px; left: 813px; }
  .label--flavored { top: 53px; --accent: var(--flavored); --title: var(--flavored); }
  .label--decaf { top: 441px; --accent: var(--decaf); --title: var(--decaf); }
  .label--harborline { top: 831px; --accent: var(--harborline); --title: var(--harborline); }
  .label--breakfast { --accent: var(--breakfast); --title: var(--breakfast-text); }

  .label__frame {
    position: absolute;
    left: 1.9em; right: 1.9em; top: 2.3em; bottom: 3.5em;
    border: 0.12em solid var(--accent);
    border-bottom: none;
    opacity: 0.85;
  }
  .label__tab {
    position: absolute;
    left: 50%; top: 0;
    width: 10.7em; height: 14.7em;
    transform: translateX(-50%);
    background: var(--accent);
  }
  .brand-seal {
    position: absolute;
    left: 50%; top: 14.7em;
    width: 18.5em; height: 18.5em;
    transform: translate(-50%, -50%);
    border-radius: 50%;
    background: var(--accent);
    display: flex; align-items: center; justify-content: center;
  }
  .brand-seal::after {
    content: "";
    position: absolute; inset: 1.2em;
    border: 0.15em solid var(--white);
    border-radius: 50%;
  }
  .brand-seal__name {
    color: var(--white);
    font-weight: 500;
    font-size: 2.3em;
    line-height: 1.15;
    text-align: center;
    letter-spacing: 0.04em;
  }
  .label__tagline {
    position: absolute;
    left: 0; right: 0; top: 24.6em;
    text-align: center;
    color: var(--accent);
    white-space: nowrap;
  }
  .label__tagline span {
    display: block;
    font-size: 0.95em;
    line-height: 1.2;
    letter-spacing: 0.08em;
  }
  .label__copy {
    position: absolute;
    left: 0; right: 0; top: 27.6em;
    display: flex; flex-direction: column; align-items: center;
    color: var(--title);
    text-align: center;
  }
  .label__title { font-weight: 700; font-size: 4em; line-height: 1.05; }
  .label__subtitle { font-weight: 400; font-size: 1.75em; line-height: 1.1; }
  .label__roaster {
    font-family: "Dancing Script", cursive;
    font-size: 3.2em; line-height: 1.15;
  }
  .label--small .label__title { font-size: 3.2em; }
  .label--small .label__subtitle { font-size: 1.6em; }
  .label--small .label__roaster { font-size: 2.9em; }
  .label--decaf .label__title { font-size: 2.9em; }

  .label__band {
    position: absolute;
    left: 0; right: 0; bottom: 0;
    height: 3.5em;
    background: var(--accent);
  }
  .label__weight {
    position: absolute;
    left: 50%; bottom: 0.6em;
    width: 17.3em; height: 4em;
    transform: translateX(-50%);
    border-radius: 2em;
    background: var(--accent);
    color: var(--white);
    font-weight: 700;
    font-size: 1em;
    display: flex; align-items: center; justify-content: center;
  }
  .label__weight span { font-size: 1.5em; }
</style>
</head>
<body>

  <section class="label label--large label--breakfast" role="img" aria-label="Green label with a faint coffee bean pattern">
    <div class="label__frame"></div>
    <div class="label__tab"></div>
    <div class="brand-seal"><p class="brand-seal__name">BRINDLE<br>MUGWORKS</p></div>
    <p class="label__tagline"><span>Small batch roasted in Alder Falls</span></p>
    <div class="label__copy">
      <h1 class="label__title">BREAKFAST BLEND</h1>
      <p class="label__subtitle">SUPREMO BLEND</p>
      <p class="label__roaster">Coffee Roaster</p>
    </div>
    <div class="label__band"></div>
    <div class="label__weight"><span>Nt. Wt:16 oz</span></div>
  </section>

  <section class="label label--small label--flavored" role="img" aria-label="Green label with a faint coffee bean pattern">
    <div class="label__frame"></div>
    <div class="label__tab"></div>
    <div class="brand-seal"><p class="brand-seal__name">BRINDLE<br>MUGWORKS</p></div>
    <p class="label__tagline"><span>Small batch roasted in Alder Falls</span></p>
    <div class="label__copy">
      <h2 class="label__title">FLAVORED COFFEES</h2>
      <p class="label__roaster">Coffee Roaster</p>
    </div>
    <div class="label__band"></div>
    <div class="label__weight"><span>Nt. Wt:16 oz</span></div>
  </section>

  <section class="label label--small label--decaf" role="img" aria-label="Green label with a faint coffee bean pattern">
    <div class="label__frame"></div>
    <div class="label__tab"></div>
    <div class="brand-seal"><p class="brand-seal__name">BRINDLE<br>MUGWORKS</p></div>
    <p class="label__tagline"><span>Small batch roasted in Alder Falls</span></p>
    <div class="label__copy">
      <h2 class="label__title">DECAFFEINATED</h2>
      <p class="label__subtitle">BLEND</p>
      <p class="label__roaster">Coffee Roaster</p>
    </div>
    <div class="label__band"></div>
    <div class="label__weight"><span>Nt. Wt:16 oz</span></div>
  </section>

  <section class="label label--small label--harborline" role="img" aria-label="Green label with a faint coffee bean pattern">
    <div class="label__frame"></div>
    <div class="label__tab"></div>
    <div class="brand-seal"><p class="brand-seal__name">BRINDLE<br>MUGWORKS</p></div>
    <p class="label__tagline"><span>Small batch roasted in Alder Falls</span></p>
    <div class="label__copy">
      <h2 class="label__title">HARBORLINE</h2>
      <p class="label__subtitle">VELVET BLEND</p>
      <p class="label__roaster">Coffee Roaster</p>
    </div>
    <div class="label__band"></div>
    <div class="label__weight"><span>Nt. Wt:16 oz</span></div>
  </section>

</body>
</html>
```